Briar Ridge Target Range wordpress theme

I want a Wordpress theme that is classy, unusual, colorful, etc. based on my attached logo files.

Font:
- Serpentine-Bold-Bold for "BRIAR RIDGE"
- BrowalliaUPC for "TARGET RANGE"

Colors (CMYK code):
- BLACK ....... 0; 0; 0; 100;
- ORANGE ... gradient from 0; 65; 97.5; 0 to 0; 39; 97.5; 0

```html
<!DOCTYPE html>
<html lang="en">
<head>
<meta charset="utf-8">
<title>Briar Ridge Target Range</title>
<link rel="stylesheet" href="https://fonts.googleapis.com/css2?family=Source+Sans+3:ital,wght@0,400;0,600;0,700;1,400&display=swap">
<style>
:root{
  --orange:#f47b20;
  --orange-light:#f9a12b;
  --ink:#333;
  --muted:#555;
  --rule:#d6d6d6;
  --tile:#7a7a7a;
  --footer-a:#2c1406;
  --footer-b:#3d1d08;
  --footer-base:#170b03;
  --white:#fff;
}
*{margin:0;padding:0;box-sizing:border-box}
html,body{width:973px;height:1200px;overflow:hidden;background:#fff}
body{font-family:"Source Sans 3",sans-serif;color:var(--ink)}
.page{position:absolute;left:0;top:0;width:1200px;height:1480px;transform:scale(0.81083);transform-origin:0 0}
.abs{position:absolute}

/* hero */
.hero{left:0;top:0;width:1200px;height:492px;background:radial-gradient(ellipse at 75% 60%,#3a2a20 0%,#1b1512 45%,#070707 100%)}
.topbar{left:642px;top:13px;color:#eee;font-size:13px}
.social{left:992px;top:10px;color:#fff;font-size:14px;font-weight:600}
.brand{left:148px;top:46px;display:flex;align-items:center;gap:6px;color:var(--orange);font-weight:700;font-size:17px;letter-spacing:.5px}
.brand i{width:12px;height:12px;background:var(--orange);display:block}
.nav{left:428px;top:55px;width:652px;height:48px;background:linear-gradient(var(--orange-light),var(--orange));display:flex;align-items:center;border-radius:2px}
.nav a{color:#fff;text-decoration:none;font-size:14px;font-weight:600;padding:0 18px;height:48px;line-height:50px;border-right:1px solid rgba(255,255,255,.35)}
.nav a:last-child{border:none}
.nav a.active{background:#fff;color:#222;padding:0 22px}
.slide-frame{left:140px;top:212px;width:438px;height:218px;background:#e6e6e6;border-radius:3px}
.slide-photo{left:16px;top:18px;width:407px;height:182px;background:linear-gradient(180deg,#2a2a30 0%,#46506a 45%,#8d5a3e 80%,#2b2220 100%)}
.slide-title{left:617px;top:220px;color:#fff;font-size:29px;line-height:27px;font-weight:400}
.slide-text{left:617px;top:284px;width:420px;color:#bdbdbd;font-size:17px;line-height:27px}
.read-more{left:618px;top:366px;width:150px;height:28px;background:linear-gradient(#f4f4f4,#cfcfcf);border-radius:2px;font-size:14px;font-weight:700;color:#222;line-height:28px;padding-left:36px}
.read-more svg{position:absolute;left:7px;top:10px}
.slider-ctrl{left:893px;top:467px;width:74px;height:25px;background:#d2d2d2;border-radius:3px 3px 0 0;display:flex}
.slider-ctrl span{flex:1;display:flex;align-items:center;justify-content:center}
.slider-ctrl span+span{border-left:1px solid #aaa}
.band{left:0;top:492px;width:1200px;height:8px;background:#cfcfcf}

/* content */
h2.section{font-weight:400;color:var(--ink)}
.welcome-h{left:123px;top:531px;font-size:29px}
.welcome-p{left:123px;top:570px;width:598px;font-size:14.6px;line-height:27px;text-indent:113px}
.welcome-p a{color:var(--orange);text-decoration:none}
.join-h{left:119px;top:708px;font-size:23px}
.feature{left:123px;width:573px;height:122px;border-bottom:1px solid var(--rule)}
.feature .photo{position:absolute;left:0;top:0;width:156px;height:104px;border-radius:2px}
.feature h3{position:absolute;left:181px;top:0;font-size:24px;font-weight:400;color:var(--muted)}
.feature p{position:absolute;left:195px;top:34px;width:358px;font-size:11.7px;line-height:18px;color:#444}
.newsletter-h{left:755px;top:533px;font-size:27px}
.email{left:752px;top:589px;width:181px;height:39px;background:#e4e4e4;font-size:13px;color:#888;line-height:39px;padding-left:9px}
.subscribe{left:933px;top:589px;width:114px;height:39px;background:linear-gradient(var(--orange-light),var(--orange));color:#fff;font-size:24px;text-align:center;line-height:38px}
.dates-h{left:752px;top:670px;font-size:21px}
.date{left:753px;width:300px;height:52px}
.tile{position:absolute;left:0;top:0;width:64px;height:52px;background:var(--tile);border-radius:3px;text-align:center;color:#fff;font-size:12px}
.tile b{display:block;margin:8px auto 3px;width:48px;height:22px;background:#fff;color:#777;border-radius:3px;font-weight:400;line-height:22px;font-size:13px}
.tile.dark{background:#111}
.tile.dark b{background:var(--orange);color:#fff}
.date h4{position:absolute;left:78px;top:0;font-size:18px;font-weight:400;color:var(--ink)}
.date small{position:absolute;left:79px;top:29px;font-size:13px;color:#444}
.schedules{left:900px;top:921px;color:var(--orange);font-size:17px}
.latest-h{left:752px;top:947px;font-size:23px}
.event{left:752px;width:296px;height:82px;border-bottom:1px solid #e2e2e2}
.event .photo{position:absolute;left:0;top:0;width:91px;height:69px}
.event h4{position:absolute;left:115px;top:4px;font-size:17px;font-weight:400}
.event span{position:absolute;left:117px;top:39px;font-size:17px;color:#555}

/* footer */
.footer{left:0;top:1212px;width:1200px;height:220px;background:linear-gradient(90deg,var(--footer-a),var(--footer-b),var(--footer-a))}
.footer h5{position:absolute;top:24px;color:#fff;font-size:17px;font-weight:700}
.links{position:absolute;left:120px;top:50px;list-style:none}
.links li{color:#eee;font-style:italic;font-size:13px;height:29.5px;display:flex;align-items:center;gap:6px}
.map{position:absolute;left:372px;top:57px;width:205px;height:149px;background:linear-gradient(135deg,#e9e6df,#d7dbd0 60%,#c6d3e0)}
.about{position:absolute;left:615px;top:51px;width:210px;color:#eee;font-style:italic;font-size:12.5px;line-height:20px}
.contact{position:absolute;left:846px;top:58px;list-style:none}
.contact li{color:#eee;font-style:italic;font-size:12.5px;height:29px;display:flex;align-items:center;gap:16px}
.contact i{width:14px;height:12px;background:#c9d3de;display:block}
.contact i.red{background:#c33}
.base{left:0;top:1432px;width:1200px;height:48px;background:var(--footer-base);border-top:1px solid #3a2a1c;font-size:13px;color:#5e5247}
.base .copy{position:absolute;left:111px;top:12px}
.base .top{position:absolute;left:1026px;top:10px}
</style>
</head>
<body>
<div class="page">
  <header class="abs hero" role="img" aria-label="Dim stadium shooting hall backdrop"></header>
  <div class="abs topbar">Call Us : 555 014 2870 &nbsp;|&nbsp; Mail : info@briarridge.com</div>
  <div class="abs social">Social</div>
  <div class="abs brand"><i></i>BRIAR RIDGE</div>
  <nav class="abs nav">
    <a>HOME</a><a>ABOUT US</a><a class="active">TRAINING</a><a>EVENTS</a><a>GALLERY</a><a>CONTACT US</a><a>BLOG</a>
  </nav>
  <div class="abs slide-frame"><div class="abs slide-photo" role="img" aria-label="Indoor shooting range with shooters at firing line"></div></div>
  <h1 class="abs slide-title">TITLE FOR SLIDE TWO ONTO<br>MULTIPLE LINES</h1>
  <p class="abs slide-text">Lorem Ipsum is simply dummy text of the printing and typesetting industry.</p>
  <div class="abs read-more"><svg width="8" height="8"><path d="M0 0L7 4L0 8Z" fill="#222"/></svg>READ MORE</div>
  <div class="abs slider-ctrl">
    <span><svg width="7" height="8"><path d="M7 0L0 4L7 8Z" fill="#333"/></svg></span>
    <span><svg width="7" height="8"><path d="M0 0L7 4L0 8Z" fill="#333"/></svg></span>
  </div>
  <div class="abs band"></div>

  <h2 class="abs section welcome-h">WELCOME</h2>
  <p class="abs welcome-p">Lorem Ipsum is simply dummy text of the printing and typesetting industry. Lorem Ipsum has been the industry's standard dummy text ever since the 1500s, when an unknown printer took a galley of type and scrambled it to make a type specimen book.Lorem Ipsum is simply dummy text of the printing and typesetting industry.....<a>[Read More</a>]</p>
  <h2 class="abs section join-h">WHY YOU SHOULD JOIN US</h2>

  <article class="abs feature" style="top:777px">
    <div class="photo" role="img" aria-label="Pistol shooter aiming at the range" style="background:linear-gradient(90deg,#3d4e6a,#8a9ab0 60%,#c9ccd0)"></div>
    <h3>Get In Shape</h3>
    <p>Quisque auctor neque a nisl sollicitudin posuere. Aliquam in enim vitae turpis euismod cursus. Aenean libero ante Quisque auctor neque a nisl sollicitudin posuere. Aliquam in enim vitae turpis euismod cursus. Aenean libero ante</p>
  </article>
  <article class="abs feature" style="top:921px">
    <div class="photo" role="img" aria-label="Smiling shooter in front of targets" style="background:linear-gradient(90deg,#6b5a34,#b09060 50%,#cfd6dc)"></div>
    <h3>Compete</h3>
    <p>Quisque auctor neque a nisl sollicitudin posuere. Aliquam in enim vitae turpis euismod cursus. Aenean libero ante Quisque auctor neque a nisl sollicitudin posuere. Aliquam in enim vitae turpis euismod cursus. Aenean libero ante</p>
  </article>
  <article class="abs feature" style="top:1067px">
    <div class="photo" role="img" aria-label="Team members celebrating with medals" style="background:linear-gradient(90deg,#7e5a48,#b7a089 50%,#5c6c48)"></div>
    <h3>Make Friends</h3>
    <p>Quisque auctor neque a nisl sollicitudin posuere. Aliquam in enim vitae turpis euismod cursus. Aenean libero ante Quisque auctor neque a nisl sollicitudin posuere. Aliquam in enim vitae turpis euismod cursus. Aenean libero ante</p>
  </article>

  <h2 class="abs section newsletter-h">NEWSLETTER</h2>
  <div class="abs email">Your Email Address</div>
  <div class="abs subscribe">Subscribe</div>
  <h2 class="abs section dates-h">UPCOMING IMPORTANT DATES</h2>
  <div class="abs date" style="top:724px"><div class="tile"><b>DEC</b>6</div><h4>Team Training</h4><small>8:00-9:00 Main Hall</small></div>
  <div class="abs date" style="top:791px"><div class="tile"><b>DEC</b>6</div><h4>Team Training</h4><small>8:00-9:00 Main Hall</small></div>
  <div class="abs date" style="top:860px"><div class="tile dark"><b>JUN</b>6</div><h4>League Match</h4><small>4:00-6:00 Statium</small></div>
  <div class="abs schedules">View Full Schedules</div>
  <h2 class="abs section latest-h">Latest Event</h2>
  <div class="abs event" style="top:1001px"><div class="photo" role="img" aria-label="Rifle shooter at a league match" style="background:linear-gradient(90deg,#8a3a8a,#b86aa8 50%,#d8d2d6)"></div><h4>League Match</h4><span>Dec,25.2013</span></div>
  <div class="abs event" style="top:1112px;border:none"><div class="photo" role="img" aria-label="Rifle shooter aiming at a league match" style="background:linear-gradient(90deg,#2a2628,#6a5a58 50%,#c0b8b0)"></div><h4>League Match</h4><span>Nov,10.2013</span></div>

  <footer class="abs footer">
    <h5 style="left:120px">IMPORTANT LINKS</h5>
    <ul class="links">
      <li><svg width="34" height="6"><path d="M0 3H30M26 0L32 3L26 6" stroke="#bbb" fill="none"/></svg>League Website</li>
      <li><svg width="34" height="6"><path d="M0 3H30M26 0L32 3L26 6" stroke="#bbb" fill="none"/></svg>Gun Shooting Rules &amp; History</li>
      <li><svg width="34" height="6"><path d="M0 3H30M26 0L32 3L26 6" stroke="#bbb" fill="none"/></svg>Training Methods &amp; Techniques</li>
      <li><svg width="34" height="6"><path d="M0 3H30M26 0L32 3L26 6" stroke="#bbb" fill="none"/></svg>League Table</li>
    </ul>
    <h5 style="left:373px">LOCATE US</h5>
    <div class="map" role="img" aria-label="Street map showing range location"></div>
    <h5 style="left:617px">ABOUT US</h5>
    <p class="about">molestie at nulla. Donec commodo lacus non dui egestas non bibendum tellus cursus. Suspendisse sit amet est odio. Suspendisse semper, turpis eget feugiat venenatis.tortor eu libero euismod vel congue ligula ullamcorper</p>
    <h5 style="left:833px">CONTACT DETAILS</h5>
    <ul class="contact">
      <li><i></i>555 014 2870</li>
      <li><i></i>info@briarridge.com</li>
      <li><i class="red"></i>Video Channel</li>
      <li><i></i>Contact Form</li>
    </ul>
  </footer>
  <div class="abs base"><span class="copy">All Right Reserved Briar Ridge</span><span class="top">Back To Top</span></div>
</div>
</body>
</html>
```